Naturopath Practitioner Card Design

I am a naturopath needing a design for a business card mainly to show that I am a naturopath and have some contact details to give to prospective clients. I am open minded about the design and what is on the second side of the card whether it just be some artwork or space for details, appointment times etc. Naturopathy is the practice of natural medicine that uses a holistic approach and incorporates herbal and nutritional medicine.

Industry/Entity Type

Business

Contact Information for Business Card

Tom Welby NaturopathBHSc (Naturopathy) Member PHRA 0492 815 306 tom.welby@mailbright.com www.tomwelbynaturopathy.com.au

Requirements
Nice to have
• Would prefer some kind of original pattern/art work/logo rather than an image, not fussed if its very simple/basic
• I am open to any colour but think I would prefer a more earthy sandy clay etc type style than the greens that are commonly associated with naturopathy.
Should not have
• Don't really want to have generic stock images on it

```html
<!DOCTYPE html>
<html lang="en">
<head>
<meta charset="utf-8">
<title>Tom Welby Naturopathy – Business Card</title>
<link href="https://fonts.googleapis.com/css2?family=Open+Sans:wght@300;400;700&display=swap" rel="stylesheet">
<style>
  :root {
    --backdrop: #e9e6e1;
    --card-white: #fbfbfa;
    --card-dark: #3a3c3c;
    --card-dark-deep: #262828;
    --sand: #c9a67a;
    --text-light: #f1f1f0;
    --rule: #6b6b6b;
  }
  * { box-sizing: border-box; margin: 0; padding: 0; }
  html, body {
    width: 1200px; height: 800px; overflow: hidden;
    background: var(--backdrop);
    font-family: "Open Sans", Arial, sans-serif;
  }
  .canvas {
    width: 1200px; height: 800px;
    display: flex; align-items: center; justify-content: center; gap: 40px;
  }
  .card {
    position: relative;
    width: 540px; height: 309px;
    overflow: hidden;
    box-shadow: 0 6px 18px rgba(0,0,0,0.18);
  }

  /* Back side: appointment card */
  .card--back { background: var(--card-white); }
  .appointment-lines {
    position: absolute; left: 28px; right: 28px; top: 28px;
    display: flex; flex-direction: column; gap: 36px;
  }
  .appointment-lines span { display: block; height: 1px; background: var(--rule); }
  .back-brand { position: absolute; left: 28px; bottom: 26px; }

  /* Brand name lockup */
  .brand { display: flex; align-items: center; gap: 12px; }
  .brand__dot {
    width: 16px; height: 16px; border-radius: 50%;
    background: var(--sand); flex: none;
  }
  .brand__name {
    color: var(--sand); font-weight: 300; font-size: 28px; line-height: 1.08;
  }

  /* Front side */
  .card--front {
    background: linear-gradient(160deg, var(--card-dark) 0%, var(--card-dark-deep) 100%);
  }
  .front-band {
    position: absolute; left: 0; right: 0; bottom: 0; height: 14px;
    background: var(--sand);
  }
  .front-brand { position: absolute; left: 38px; top: 44px; }
  .contact {
    position: absolute; left: 300px; top: 104px;
    color: var(--text-light);
  }
  .contact__name {
    color: var(--sand); font-weight: 700; font-size: 15px; letter-spacing: 0.5px;
  }
  .contact__title { font-size: 11px; margin: 3px 0 10px; }
  .contact__row {
    display: flex; align-items: center; gap: 7px;
    font-size: 11.5px; line-height: 1; margin-bottom: 6px;
  }
  .contact__icon { width: 12px; height: 12px; flex: none; }
</style>
</head>
<body>
<main class="canvas">

  <section class="card card--back" aria-label="Card back – appointment side">
    <div class="appointment-lines">
      <span></span><span></span><span></span><span></span>
    </div>
    <div class="back-brand brand">
      <span class="brand__dot"></span>
      <span class="brand__name">Tom Welby<br>Naturopathy</span>
    </div>
  </section>

  <section class="card card--front" aria-label="Card front – contact side">
    <div class="front-brand brand">
      <span class="brand__dot"></span>
      <span class="brand__name">Tom Welby<br>Naturopathy</span>
    </div>

    <div class="contact">
      <p class="contact__name">TOM WELBY</p>
      <p class="contact__title">NaturopathBHSc | Member PHRA</p>
      <p class="contact__row">
        <svg class="contact__icon" viewBox="0 0 12 12" aria-hidden="true"><circle cx="6" cy="6" r="6" fill="#c9a67a"/><path d="M4 3.2 L5 3 L5.6 4.6 L5 5.1 C5.3 5.9 6.1 6.7 6.9 7 L7.4 6.4 L9 7 L8.8 8 C6.5 8.4 3.6 5.5 4 3.2 Z" fill="#2e3030"/></svg>
        0492 815 306
      </p>
      <p class="contact__row">
        <svg class="contact__icon" viewBox="0 0 12 12" aria-hidden="true"><circle cx="6" cy="6" r="6" fill="#c9a67a"/><rect x="3" y="4" width="6" height="4.2" fill="none" stroke="#2e3030" stroke-width="0.9"/><path d="M3 4 L6 6.3 L9 4" fill="none" stroke="#2e3030" stroke-width="0.9"/></svg>
        tom.welby@mailbright.com
      </p>
      <p class="contact__row">
        <svg class="contact__icon" viewBox="0 0 12 12" aria-hidden="true"><circle cx="6" cy="6" r="6" fill="#c9a67a"/><circle cx="6" cy="6" r="3.3" fill="none" stroke="#2e3030" stroke-width="0.8"/><ellipse cx="6" cy="6" rx="1.4" ry="3.3" fill="none" stroke="#2e3030" stroke-width="0.8"/><path d="M2.7 6 H9.3" stroke="#2e3030" stroke-width="0.8"/></svg>
        www.tomwelbynaturopathy.com.au
      </p>
    </div>

    <div class="front-band"></div>
  </section>

</main>
</body>
</html>
```